Business Card Design

I need a business card designed for my new company BrightOak Home developments I specialise in all aspects of carpentry including Decks, Pergolas, Conventional Framing and fit outs I am open to different colours as long as it fits with my logo.

Industry/Entity Type

Carpentry

Contact Information for Business Card

BrightOak Home Developments, Greg Mollory, 0461802394, specialising in all aspects of carpentry and construction

```html
<!DOCTYPE html>
<html lang="en">
<head>
<meta charset="utf-8">
<title>BrightOak Home Developments — Business Card</title>
<link rel="stylesheet" href="https://fonts.googleapis.com/css2?family=Caladea:wght@400;700&display=swap">
<style>
  :root {
    --blue: #1257a8;
    --blue-text: #1452a3;
    --charcoal: #2a2a2a;
    --white: #ffffff;
    --backdrop: #e9e8e6;
    --band-shadow: 0 0 10px rgba(0, 0, 0, 0.45);
  }
  * { box-sizing: border-box; margin: 0; padding: 0; }
  html, body {
    width: 1129px;
    height: 1200px;
    overflow: hidden;
  }
  body {
    background: var(--backdrop);
    font-family: "Caladea", Georgia, serif;
    position: relative;
  }
  .card {
    position: absolute;
    left: 161px;
    width: 808px;
    background: var(--blue);
    overflow: hidden;
    box-shadow: 0 6px 18px rgba(0, 0, 0, 0.25);
  }
  .card--front { top: 96px; height: 471px; }
  .card--back { top: 636px; height: 464px; }

  .band { position: absolute; }
  .band--dark { background: var(--charcoal); box-shadow: var(--band-shadow); }
  .band--white { background: var(--white); box-shadow: var(--band-shadow); }

  /* Front */
  .front__column { left: 20px; top: 0; width: 172px; height: 100%; z-index: 2; }
  .front__name-band {
    left: 192px; top: 37px; width: 616px; height: 96px;
    display: flex; align-items: center; justify-content: center;
    z-index: 1;
  }
  .front__name {
    color: var(--blue-text);
    font-size: 52px;
    font-weight: 700;
    letter-spacing: 0.5px;
  }
  .front__services {
    position: absolute;
    left: 192px; top: 150px; width: 616px;
    color: var(--white);
  }
  .services__heading {
    display: flex; align-items: center; gap: 16px;
    font-size: 28px; font-weight: 700;
    padding: 0 12px;
  }
  .services__heading::before,
  .services__heading::after {
    content: ""; flex: 1; height: 1px; background: rgba(255, 255, 255, 0.7);
  }
  .services__list {
    list-style: none;
    display: grid;
    grid-template-columns: 192px 260px;
    margin: 14px 0 0 101px;
    font-size: 22px; font-weight: 700; line-height: 28px;
  }
  .services__note {
    text-align: center;
    font-size: 22px; font-weight: 700;
    margin-top: 22px;
  }
  .front__contact-band {
    left: 0; top: 335px; width: 808px; height: 78px;
    display: flex; align-items: center; justify-content: center;
    padding-left: 180px;
    z-index: 1;
  }
  .contact__phone {
    display: flex; align-items: center; gap: 8px;
    color: var(--white);
    font-size: 23px; font-weight: 700;
    letter-spacing: 0.5px;
  }

  /* Back */
  .back__top-band { left: 0; top: 0; width: 808px; height: 77px; z-index: 2; }
  .back__panel {
    left: 20px; top: 77px; width: 771px; height: 250px;
    display: flex; align-items: center; justify-content: center; gap: 18px;
    z-index: 1;
  }
  .brand__mark { width: 22px; height: 22px; background: var(--blue-text); }
  .brand__name {
    color: var(--blue-text);
    font-size: 46px;
    font-weight: 400;
    letter-spacing: 1px;
  }
  .back__lower-band { left: 0; top: 331px; width: 808px; height: 76px; z-index: 2; }
  .back__corner-block { left: 619px; top: 331px; width: 173px; height: 133px; z-index: 1; }
</style>
</head>
<body>

<section class="card card--front" aria-label="Business card front">
  <div class="band band--dark front__column"></div>
  <div class="band band--white front__name-band">
    <h1 class="front__name">Greg Mollory</h1>
  </div>
  <div class="front__services">
    <h2 class="services__heading">Specialising In</h2>
    <ul class="services__list">
      <li>Decks</li>
      <li>Conventional Framing</li>
      <li>Pergolas</li>
      <li>Fit Outs</li>
    </ul>
    <p class="services__note">...and all aspects of carpentry and construction!</p>
  </div>
  <div class="band band--dark front__contact-band">
    <p class="contact__phone">
      <svg width="24" height="24" viewBox="0 0 24 24" aria-hidden="true">
        <circle cx="12" cy="12" r="12" fill="#ffffff"/>
        <path d="M8.2 5.5c.5-.3 1.1-.2 1.4.3l1.3 2.2c.3.5.2 1.1-.3 1.4l-.9.6c.5 1.7 1.7 3.3 3.2 4.3l.8-.7c.4-.4 1.1-.4 1.5 0l1.8 1.8c.4.4.4 1.1 0 1.5l-1 1c-.8.8-2 1-3 .5-3.1-1.6-5.5-4.4-6.5-7.8-.3-1.1.1-2.3 1-2.9z" fill="#1257a8"/>
      </svg>
      0461802394
    </p>
  </div>
</section>

<section class="card card--back" aria-label="Business card back">
  <div class="band band--dark back__top-band"></div>
  <div class="band band--white back__panel">
    <span class="brand__mark" aria-hidden="true"></span>
    <p class="brand__name">BrightOak Home Developments</p>
  </div>
  <div class="band band--dark back__lower-band"></div>
  <div class="band band--dark back__corner-block"></div>
</section>

</body>
</html>
```